Clean Stationary Design For Print Shop

I need a clean stationary set that properly represents a local print and copy shop to make it look amazing. It should do the following:
- Compliment the color scheme of the logo.
- Be clean and sharp.
- Be colorful but but balanced.

This is what I need designed:
- Business Card
- Letter Head
- Envelop

Target Market(s)

Local customers and businesses, including hospitals and schools.

Industry/Entity Type

Digital Printing

Requirements
Must have
• Clean business card with logo on front and full color back with faded logo on it and social icons with @tollworthmarks beside each one (Pagelark & Glimmora).

```html
<!DOCTYPE html>
<html lang="en">
<head>
<meta charset="utf-8">
<title>Tollworth Marks Stationery</title>
<link href="https://fonts.googleapis.com/css2?family=Open+Sans:wght@400;600;700&display=swap" rel="stylesheet">
<style>
:root{
  --bg:#eceded;
  --paper:#ffffff;
  --ink:#1c1c1e;
  --text:#4a4a4c;
  --muted:#8b8b8e;
  --red:#e33a50;
  --red-faint:#f6dde0;
  --black:#1a1a1a;
}
*{box-sizing:border-box;margin:0;padding:0}
html,body{width:899px;height:1200px;overflow:hidden}
body{background:var(--bg);font-family:"Open Sans",Arial,sans-serif;color:var(--text);position:relative}
.sheet{position:absolute;background:var(--paper);box-shadow:0 2px 6px rgba(0,0,0,.12);overflow:hidden}

.brand{display:flex;align-items:center;gap:6px}
.brand-mark{width:12px;height:12px;background:var(--red);flex:none}
.brand-name{font-weight:600;color:var(--ink);font-size:17px;letter-spacing:-.2px;white-space:nowrap}
.brand-tagline{font-size:5.5px;letter-spacing:1px;text-transform:uppercase;color:var(--muted);margin-left:18px;margin-top:1px;font-weight:600;white-space:nowrap}
.on-dark .brand-name{color:#fff}
.on-dark .brand-tagline{color:#cfcfcf}

.bands{position:absolute;left:0;bottom:0;width:100%}

/* letterhead */
.letterhead{left:40px;top:34px;width:390px;height:552px}
.letterhead .brand-block{position:absolute;left:150px;top:56px}
.letter-body{position:absolute;left:42px;right:42px;top:150px;font-size:6.6px;line-height:1.6}
.letter-body p{margin-bottom:9px}
.letter-sign{width:46px;height:26px;background:#f3f3f3;margin-top:4px;border-radius:3px}
.letter-footer{position:absolute;right:34px;bottom:38px;text-align:right;font-size:7px;line-height:1.7;color:var(--ink)}
.contact-row{display:inline-flex;align-items:center;gap:3px;margin-left:8px;white-space:nowrap}
.contact-row svg{width:7px;height:7px;fill:var(--red);flex:none}

/* business cards */
.card{width:360px;height:206px}
.card-front{left:490px;top:70px}
.card-front .brand-block{position:absolute;left:24px;top:88px}
.card-details{position:absolute;left:212px;top:44px;font-size:7px;line-height:1.75;color:var(--ink)}
.card-name{color:var(--red);font-weight:700;font-size:9px;text-transform:uppercase;letter-spacing:.4px}
.card-role{font-weight:600;font-size:6.5px;text-transform:uppercase;color:var(--muted);margin-bottom:6px}
.card-details .contact-row{margin-left:0;display:flex}
.card-back{left:490px;top:320px;background:var(--black)}
.card-back .brand-block{position:absolute;left:90px;top:72px}
.social{position:absolute;left:108px;top:130px;display:flex;gap:14px;font-size:7.5px;color:#fff}
.social-item{display:flex;align-items:center;gap:4px}
.social-dot{width:8px;height:8px;border-radius:50%;background:var(--red)}

/* envelopes */
.envelope{width:520px;height:254px}
.envelope-front{left:40px;top:640px}
.envelope-front .brand-block{position:absolute;left:26px;top:26px}
.env-address{position:absolute;left:44px;top:78px;font-size:7px;line-height:1.7;color:var(--ink)}
.env-address .contact-row{margin-left:0;display:flex}
.faded-mark{position:absolute;right:52px;top:96px;width:130px;height:130px;background:var(--red-faint)}
.envelope-back{left:339px;top:918px}
.env-flap{position:absolute;left:0;top:0;width:100%;height:70px;background:var(--black)}
.env-flap .brand-block{position:absolute;left:190px;top:20px}
</style>
</head>
<body>

<section class="sheet letterhead" aria-label="Letterhead">
  <div class="brand-block">
    <div class="brand"><span class="brand-mark"></span><span class="brand-name">Tollworth Marks</span></div>
    <div class="brand-tagline">Sharp prints, quick turnaround</div>
  </div>
  <div class="letter-body">
    <p>Dear Customer,</p>
    <p>Lorem ipsum dolor sit amet, consectetur adipisicing elit, sed do eiusmod tempor incididunt ut labore et dolore magna aliqua. Ut enim ad minim veniam, quis nostrud exercitation ullamco laboris nisi ut aliquip ex ea commodo consequat. Duis aute irure dolor in reprehenderit in voluptate velit esse cillum dolore eu fugiat nulla pariatur. Excepteur sint occaecat cupidatat non proident, sunt in culpa qui officia deserunt mollit anim id est laborum.</p>
    <p>Lorem ipsum dolor sit amet, consectetur adipisicing elit, sed do eiusmod tempor incididunt ut labore et dolore magna aliqua. Ut enim ad minim veniam, quis nostrud exercitation ullamco laboris nisi ut aliquip ex ea commodo consequat. Duis aute irure dolor in reprehenderit in voluptate velit esse cillum dolore eu fugiat nulla pariatur. Excepteur sint occaecat cupidatat non proident, sunt in culpa qui officia deserunt mollit anim id est laborum.</p>
    <p>Lorem ipsum dolor sit amet, consectetur adipisicing elit, sed do eiusmod tempor incididunt ut labore et dolore magna aliqua. Ut enim ad minim veniam, quis nostrud exercitation ullamco laboris nisi ut aliquip ex ea commodo consequat. Duis aute irure dolor in reprehenderit.</p>
    <p>Lorem ipsum dolor sit amet, consectetur adipisicing elit, sed do eiusmod tempor incididunt ut labore et dolore magna aliqua. Ut enim ad minim veniam, quis nostrud exercitation ullamco laboris nisi ut aliquip ex ea commodo consequat.</p>
    <p>Yours Sincerely,</p>
    <div class="letter-sign" role="img" aria-label="Handwritten signature"></div>
  </div>
  <div class="letter-footer">
    <div>2170 Harlow Mill Road Brookfield, Oh 45311</div>
    <div>
      <span class="contact-row"><svg viewBox="0 0 10 10"><path d="M2 1h2l1 2.5-1.2.8a5 5 0 0 0 2 2l.8-1.2L9 6v2a1 1 0 0 1-1 1A7 7 0 0 1 1 2a1 1 0 0 1 1-1z"/></svg>555.208.4417</span>
      <span class="contact-row"><svg viewBox="0 0 10 10"><path d="M0 2h10v6H0zM0 2l5 3.5L10 2v1L5 6.5 0 3z"/></svg>hello@tollworthmarks.com</span>
      <span class="contact-row"><svg viewBox="0 0 10 10"><circle cx="5" cy="5" r="5"/></svg>www.tollworthmarks.com</span>
    </div>
  </div>
  <svg class="bands" viewBox="0 0 390 24" height="24" preserveAspectRatio="none">
    <polygon points="0,16 390,16 390,24 0,24" fill="#1a1a1a"/>
    <polygon points="310,8 390,8 390,13 306,13" fill="#e33a50"/>
    <polygon points="0,13 306,13 304,15 0,15" fill="#1a1a1a"/>
  </svg>
</section>

<section class="sheet card card-front" aria-label="Business card front">
  <div class="brand-block">
    <div class="brand"><span class="brand-mark"></span><span class="brand-name" style="font-size:14px">Tollworth Marks</span></div>
    <div class="brand-tagline">Sharp prints, quick turnaround</div>
  </div>
  <div class="card-details">
    <div class="card-name">Daniel Ashcroft</div>
    <div class="card-role">Managing Director</div>
    <div>2170 Harlow Mill Road</div>
    <div>Brookfield, Oh 45311</div>
    <div class="contact-row"><svg viewBox="0 0 10 10"><path d="M2 1h2l1 2.5-1.2.8a5 5 0 0 0 2 2l.8-1.2L9 6v2a1 1 0 0 1-1 1A7 7 0 0 1 1 2a1 1 0 0 1 1-1z"/></svg>555.208.4417</div>
    <div class="contact-row"><svg viewBox="0 0 10 10"><path d="M0 2h10v6H0zM0 2l5 3.5L10 2v1L5 6.5 0 3z"/></svg>hello@tollworthmarks.com</div>
    <div class="contact-row"><svg viewBox="0 0 10 10"><circle cx="5" cy="5" r="5"/></svg>www.tollworthmarks.com</div>
  </div>
  <svg class="bands" viewBox="0 0 360 20" height="20" preserveAspectRatio="none">
    <polygon points="0,14 360,14 360,20 0,20" fill="#1a1a1a"/>
    <polygon points="290,6 360,6 360,11 286,11" fill="#e33a50"/>
  </svg>
</section>

<section class="sheet card card-back on-dark" aria-label="Business card back">
  <div class="brand-block">
    <div class="brand"><span class="brand-mark"></span><span class="brand-name" style="font-size:16px">Tollworth Marks</span></div>
    <div class="brand-tagline">Sharp prints, quick turnaround</div>
  </div>
  <div class="social">
    <span class="social-item"><span class="social-dot" role="img" aria-label="Pagelark"></span>@tollworthmarks</span>
    <span class="social-item"><span class="social-dot" role="img" aria-label="Glimmora"></span>@tollworthmarks</span>
  </div>
</section>

<section class="sheet envelope envelope-front" aria-label="Envelope front">
  <div class="faded-mark" role="img" aria-label="Faded brand decoration"></div>
  <div class="brand-block">
    <div class="brand"><span class="brand-mark"></span><span class="brand-name">Tollworth Marks</span></div>
    <div class="brand-tagline">Sharp prints, quick turnaround</div>
  </div>
  <div class="env-address">
    <div>2170 Harlow Mill Road</div>
    <div>Brookfield, Oh 45311</div>
    <div class="contact-row"><svg viewBox="0 0 10 10"><path d="M2 1h2l1 2.5-1.2.8a5 5 0 0 0 2 2l.8-1.2L9 6v2a1 1 0 0 1-1 1A7 7 0 0 1 1 2a1 1 0 0 1 1-1z"/></svg>555.208.4417</div>
    <div class="contact-row"><svg viewBox="0 0 10 10"><path d="M0 2h10v6H0zM0 2l5 3.5L10 2v1L5 6.5 0 3z"/></svg>hello@tollworthmarks.com</div>
    <div class="contact-row"><svg viewBox="0 0 10 10"><circle cx="5" cy="5" r="5"/></svg>www.tollworthmarks.com</div>
  </div>
  <svg class="bands" viewBox="0 0 520 22" height="22" preserveAspectRatio="none">
    <polygon points="0,16 520,16 520,22 0,22" fill="#1a1a1a"/>
    <polygon points="440,6 520,6 520,12 434,12" fill="#e33a50"/>
    <polygon points="0,12 434,12 432,14 0,14" fill="#1a1a1a"/>
  </svg>
</section>

<section class="sheet envelope envelope-back on-dark" aria-label="Envelope back">
  <div class="env-flap">
    <div class="brand-block">
      <div class="brand"><span class="brand-mark"></span><span class="brand-name">Tollworth Marks</span></div>
      <div class="brand-tagline">Sharp prints, quick turnaround</div>
    </div>
  </div>
</section>

</body>
</html>
```